UK landscaping company needs website

We, Brindle Landscapes need a website design for a company based in Surrey, UK. The design should be bold and playful. We have three main areas of work driveways, paving and fencing. It shouldn't be too heavy in text and concentrate on the pictures from previous jobs we've completed. You may use stock images for the design, these can be changed if you are successful. Please don’t just copy the flyer it is just there to provide content.
We have a logo design which we would also like editing slightly.
Here are some of my local competitors
https://www.vexmoorlandscapes.co.uk/

https://www.twinreedgardendesign.com/

https://quarnelllandscapes.co.uk/

Industry/Entity Type

Landscaping

Coding

Coded - Design and coding required

Number of Pages Required

3 page

Font styles to use
Sans Serif

Requirements
Must have
• Pictures of my previous jobs.
Must be mobile friendly
Easy to navigate
Nice to have
• Try to use different colours. It would be good to have some designs that aren’t just black and green.
I’d like some curves in the design.
Should not have
• We install hard landscaping. Think more building/construction and less plants and cutting grass.

```html
<!DOCTYPE html>
<html lang="en">
<head>
<meta charset="utf-8">
<title>Brindle Landscapes – Garden Construction</title>
<link rel="stylesheet" href="https://fonts.googleapis.com/css2?family=Poppins:wght@400;500;600&family=Lato:wght@400;700&display=swap">
<style>
:root{
  --green:#5b7f36;
  --green-dark:#4e6f2d;
  --panel:#e3e9dc;
  --hero-box:rgba(232,240,224,.92);
  --ink:#3b3b3b;
  --muted:#8a8a8a;
  --white:#ffffff;
  --map:#d9d9d9;
}
*{margin:0;padding:0;box-sizing:border-box}
html,body{width:1200px;height:1200px;overflow:hidden;background:var(--white)}
body{font-family:"Lato",sans-serif;color:var(--ink)}
.stage{position:absolute;left:0;top:0;width:1264px;height:1264px;transform:scale(.94937);transform-origin:0 0}
.abs{position:absolute}
.photo{position:absolute}

.site-header{left:421px;top:0;width:422px;height:33px;background:var(--green)}
.brand{position:absolute;font-family:"Poppins",sans-serif;font-weight:600;color:var(--white);font-size:13px;letter-spacing:-.3px}
.site-header .brand{left:30px;top:7px}
.main-nav{position:absolute;left:243px;top:12px;display:flex;gap:13px;font-size:6px;font-weight:700;color:var(--white)}
.main-nav .active{color:#a9c48a;font-weight:400}

.hero-photo{left:574px;top:45px;width:269px;height:268px;background:linear-gradient(180deg,#aebfd2 0%,#d7dde3 30%,#8a9873 50%,#b9ad98 70%,#a69a86 100%)}
.eyebrow{position:absolute;font-size:4px;letter-spacing:.6px;color:var(--muted);text-transform:uppercase;display:flex;align-items:center;gap:4px}
.eyebrow i{display:inline-block;width:17px;height:1px;background:var(--muted)}
.hero-box{left:449px;top:114px;width:250px;height:72px;background:var(--hero-box)}
.hero-title{position:absolute;left:12px;top:3px;font-family:"Poppins",sans-serif;font-weight:400;font-size:37px;line-height:31px;color:var(--green);white-space:nowrap}
.btn{position:absolute;background:var(--green);color:var(--white);font-size:4.5px;letter-spacing:.4px;display:flex;align-items:center;justify-content:center;text-transform:uppercase}

.shot-flowers{left:544px;top:348px;width:114px;height:68px;background:linear-gradient(135deg,#7a9a45,#c45d86 45%,#9aa07a 70%,#5f7d39)}
.shot-patio{left:668px;top:327px;width:144px;height:41px;background:linear-gradient(90deg,#6c8a3e,#7b7f86 45%,#b2c640 70%,#4a5a3a)}
.shot-pool{left:543px;top:428px;width:178px;height:103px;background:linear-gradient(180deg,#b8c6c8 0%,#7b8a5c 35%,#5a4838 65%,#3d6f86 100%);z-index:2}

.services{left:449px;top:512px;width:366px;height:136px;background:var(--green);color:var(--white)}
.section-title{position:absolute;font-family:"Poppins",sans-serif;font-size:13px;font-weight:400}
.services .section-title{left:21px;top:32px}
.service{position:absolute;display:flex;align-items:center;gap:5px;font-size:6px}
.service .ico{width:22px;height:22px;border-radius:50%;background:var(--white);display:flex;align-items:center;justify-content:center}

.about-title{left:449px;top:694px;color:var(--green)}
.about-col{position:absolute;top:715px;width:176px;font-size:6px;line-height:9px;color:var(--ink)}

.contact{left:449px;top:785px;width:366px;height:249px;background:var(--panel)}
.contact .section-title{color:var(--green);top:35px}
.small{position:absolute;font-size:5px;color:var(--ink)}
.phone{position:absolute;left:21px;top:76px;display:flex;align-items:center;gap:4px;font-family:"Poppins",sans-serif;font-size:12px;color:var(--green)}
.info-label{position:absolute;font-size:6px;color:var(--green)}
.field-label{position:absolute;left:198px;font-size:4.5px;color:var(--ink)}
.field{position:absolute;left:198px;width:146px;height:15px;background:var(--white);font-size:4px;color:#aaa;padding:5px 5px}

.map{left:421px;top:1060px;width:422px;height:118px;background:linear-gradient(90deg,#d6d6d6,#c9c9c9 40%,#bfbfbf 60%,#d8d8d8)}

.site-footer{left:421px;top:1178px;width:422px;height:86px;background:var(--green);color:var(--white)}
.site-footer .brand{left:61px;top:21px}
.footer-nav{position:absolute;left:151px;top:29px;display:flex;gap:14px;font-size:4.5px}
.follow{position:absolute;left:304px;top:27px;display:flex;align-items:center;gap:4px;font-size:4.5px}
.follow b{display:inline-block;width:6px;height:6px;border-radius:50%;background:var(--white)}
.footer-rule{position:absolute;left:59px;top:52px;width:304px;height:1px;background:rgba(255,255,255,.6)}
.copyright{position:absolute;left:0;width:422px;top:72px;text-align:center;font-size:3.8px}
</style>
</head>
<body>
<div class="stage">

  <header class="abs site-header">
    <div class="brand">BRINDLE</div>
    <nav class="main-nav"><span class="active">Home</span><span>Driveways</span><span>Paving</span><span>Fencing</span></nav>
  </header>

  <div class="photo hero-photo" role="img" aria-label="Cobbled driveway in front of a house with garages"></div>
  <div class="eyebrow" style="left:449px;top:99px">01 <i></i> Landscape Solutions</div>
  <div class="abs hero-box"><h1 class="hero-title">Garden<br>Construction</h1></div>
  <a class="btn" style="left:449px;top:202px;width:66px;height:14px">Contact us</a>

  <div class="photo shot-flowers" role="img" aria-label="Stone path through a flowering garden"></div>
  <div class="photo shot-patio" role="img" aria-label="Paved patio with outdoor sofa"></div>
  <div class="photo shot-pool" role="img" aria-label="Pool terrace with gazebo and palms"></div>

  <section class="abs services">
    <h2 class="section-title">Our Services</h2>
    <div class="service" style="left:22px;top:58px"><span class="ico"><svg width="10" height="10" viewBox="0 0 10 10"><path d="M3 1h4l2 8H1z" fill="#5b7f36"/><rect x="4.6" y="2" width=".8" height="6" fill="#fff"/></svg></span>Driveways</div>
    <div class="service" style="left:147px;top:59px"><span class="ico"><svg width="10" height="10" viewBox="0 0 10 10"><path d="M2 6h6l-1 3H3z" fill="#5b7f36"/><path d="M5 6V2M5 3l-2-1M5 3l2-1" stroke="#5b7f36" fill="none"/></svg></span>Garden Design</div>
    <div class="service" style="left:272px;top:59px"><span class="ico"><svg width="10" height="10" viewBox="0 0 10 10" fill="none" stroke="#5b7f36" stroke-width=".9"><rect x="1" y="1.5" width="8" height="7"/><path d="M1 4h8M1 6.5h8M5 1.5V4M3 4v2.5M7 4v2.5M5 6.5v2"/></svg></span>Paving &amp; Brickwork</div>
    <div class="service" style="left:22px;top:90px"><span class="ico"><svg width="10" height="10" viewBox="0 0 10 10" fill="none" stroke="#5b7f36" stroke-width="1"><path d="M5 9V3M5 5L2 3M5 5l3-2M5 7L2 5.5M5 7l3-1.5"/></svg></span>Planting &amp; Turfing</div>
    <div class="service" style="left:148px;top:89px"><span class="ico"><svg width="10" height="10" viewBox="0 0 10 10" fill="none" stroke="#5b7f36" stroke-width="1.1"><path d="M2.5 1v8M5 1v8M7.5 1v8M1 3.5h8M1 6.5h8"/></svg></span>Fencing &amp; Decking</div>
    <div class="service" style="left:272px;top:90px"><span class="ico"><svg width="10" height="10" viewBox="0 0 10 10" fill="none" stroke="#5b7f36" stroke-width="1"><path d="M5 9V2M5 9L2 3M5 9l3-6M5 9L1 5M5 9l4-4"/></svg></span>Artificial Grass</div>
  </section>

  <div class="eyebrow" style="left:449px;top:679px">02 <i></i> Who we are</div>
  <h2 class="section-title abs about-title">About Us</h2>
  <p class="about-col" style="left:449px">We at Brindle Landscapes are a professional, experienced landscaping business that delivers premium garden construction at an affordable price. We provide all aspects of hard and soft landscaping throughout Surrey and surrounding areas.</p>
  <p class="about-col" style="left:637px">We pride ourselves on excellent workmanship and attention to detail. Using only top quality materials to ensure an outstanding and long-lasting finish. Installed using both traditional and modern techniques.</p>

  <section class="abs contact">
    <div class="eyebrow" style="left:21px;top:19px">03 <i></i> Get in touch</div>
    <h2 class="section-title" style="left:21px">Contact Details</h2>
    <h2 class="section-title" style="left:198px">Have A Question?</h2>
    <p class="small" style="left:22px;top:66px">Call us now for a free estimate.</p>
    <div class="phone"><svg width="12" height="12" viewBox="0 0 12 12"><path d="M2.5 1l2 2.3-1 1.3c.7 1.5 1.8 2.6 3.2 3.3l1.2-1 2.3 1.8-1 2c-4.5-.3-8-3.8-8.2-8.3z" fill="#5b7f36"/></svg>07700 900 482</div>
    <p class="info-label" style="left:25px;top:109px">Location</p>
    <p class="small" style="left:25px;top:121px;line-height:7px">48 Kiln Lane<br>Surrey, UK GU1 4RT</p>
    <p class="info-label" style="left:92px;top:109px">Email</p>
    <p class="small" style="left:92px;top:121px">info@brindle-landscapes.com</p>

    <p class="field-label" style="top:63px">Name*</p>
    <div class="field" style="top:71px">Your Name</div>
    <p class="field-label" style="top:91px">Email*</p>
    <div class="field" style="top:99px">Your Email</div>
    <p class="field-label" style="top:120px">Subject*</p>
    <div class="field" style="top:128px">Your Subject</div>
    <p class="field-label" style="top:148px">Message*</p>
    <div class="field" style="top:156px;height:51px">Your Message</div>
    <a class="btn" style="left:198px;top:216px;width:66px;height:14px">Submit message</a>
  </section>

  <div class="photo map" role="img" aria-label="Map of Surrey and surrounding area"></div>

  <footer class="abs site-footer">
    <div class="brand">BRINDLE</div>
    <nav class="footer-nav"><span>Home</span><span>Driveways</span><span>Paving</span><span>Fencing</span></nav>
    <div class="follow">Follow Us: <b></b><b></b><b></b></div>
    <div class="footer-rule"></div>
    <p class="copyright">© 2020 Brindle Landscapes. All Rights Reserved. Privacy Policy.</p>
  </footer>

</div>
</body>
</html>
```